Maple Hollow Canine Massage Needs a Business Card Design

Maple Hollow Canine Massage is a new therapeutic canine massage company located in Nederland, Colorado. I need a business card design that include my logo and basic contact information.

Target Market(s)

Pet owners, veterinarians

Industry/Entity Type

Business

Contact Information for Business Card

Lydia Ferrow, CCMT
303.518.7269
lydia@maplehollowmassage.example
www.maplehollowmassage.example

Colors
6c459b
886aae
b8a6cd
a64599
b768aa
d3a5cc
fbed22

Requirements
Must have
• Font should be similar to font in logo.

```html
<!DOCTYPE html>
<html lang="en">
<head>
<meta charset="utf-8">
<title>Maple Hollow Canine Massage – Business Card</title>
<link rel="stylesheet" href="https://fonts.googleapis.com/css2?family=Montserrat:wght@700&family=Source+Sans+3:wght@400;600&display=swap">
<style>
  :root {
    --violet-deep: #6c459b;
    --violet-mid: #886aae;
    --violet-soft: #b8a6cd;
    --gold: #fbed22;
    --ink: #1f1a24;
    --paper: #ffffff;
    --backdrop: #e9e6ec;
  }
  * { box-sizing: border-box; margin: 0; padding: 0; }
  html, body { width: 1200px; height: 844px; overflow: hidden; }
  body {
    background: var(--backdrop);
    font-family: "Source Sans 3", "Helvetica Neue", Arial, sans-serif;
    position: relative;
  }
  .card {
    position: absolute;
    top: 279px;
    width: 500px;
    height: 286px;
    border-radius: 4px;
    box-shadow: 0 10px 28px rgba(40, 20, 60, 0.18);
    overflow: hidden;
  }
  .card--front { left: 60px; background: var(--paper); }
  .card--back {
    left: 640px;
    background: linear-gradient(135deg, #a985cc 0%, var(--violet-mid) 45%, var(--violet-deep) 100%);
  }

  /* Front */
  .brand-mark {
    position: absolute;
    top: 22px;
    right: 26px;
    width: 140px;
    display: flex;
    flex-direction: column;
    align-items: center;
    gap: 8px;
  }
  .brand-mark__dot {
    width: 72px;
    height: 72px;
    border-radius: 50%;
    background: var(--violet-mid);
  }
  .brand-mark__name {
    font-family: "Montserrat", "Helvetica Neue", Arial, sans-serif;
    font-weight: 700;
    font-size: 13px;
    line-height: 1.25;
    text-align: center;
    color: var(--violet-deep);
    letter-spacing: 0.02em;
  }
  .contact {
    position: absolute;
    left: 34px;
    bottom: 30px;
  }
  .contact__name {
    font-weight: 600;
    font-size: 22px;
    color: var(--violet-deep);
    margin-bottom: 12px;
  }
  .contact__name small {
    font-size: 13px;
    font-weight: 400;
    color: var(--violet-mid);
  }
  .contact__list { list-style: none; }
  .contact__item {
    display: flex;
    align-items: center;
    gap: 10px;
    font-size: 15px;
    color: var(--ink);
    line-height: 1.55;
  }
  .contact__icon { width: 12px; height: 12px; fill: var(--violet-deep); flex: none; }

  /* Back */
  .back-title {
    position: absolute;
    left: 0;
    right: 0;
    top: 122px;
    text-align: center;
    font-family: "Montserrat", "Helvetica Neue", Arial, sans-serif;
    font-weight: 700;
    color: var(--paper);
    font-size: 26px;
    line-height: 1.3;
    letter-spacing: 0.03em;
  }
  .back-title span { display: block; font-size: 26px; }
</style>
</head>
<body>
  <section class="card card--front" aria-label="Business card front">
    <div class="brand-mark">
      <div class="brand-mark__dot"></div>
      <div class="brand-mark__name">Maple Hollow<br>Canine Massage</div>
    </div>
    <div class="contact">
      <p class="contact__name">Lydia Ferrow, <small>CCMT</small></p>
      <ul class="contact__list">
        <li class="contact__item">
          <svg class="contact__icon" viewBox="0 0 12 12" aria-hidden="true"><path d="M2.4 0.6 4.2 2.6 3.3 4c.6 1.5 1.9 2.8 3.4 3.5l1.4-.9 2 1.8-1.2 1.9C5 10 1.6 6.3 1.3 2.2z"/></svg>
          303.518.7269
        </li>
        <li class="contact__item">
          <svg class="contact__icon" viewBox="0 0 12 12" aria-hidden="true"><path d="M0.5 2.5h11v7h-11z M1 3l5 3.8L11 3" fill="var(--violet-deep)" stroke="#fff" stroke-width="0.8"/></svg>
          lydia@maplehollowmassage.example
        </li>
        <li class="contact__item">
          <svg class="contact__icon" viewBox="0 0 12 12" aria-hidden="true"><circle cx="6" cy="6" r="5.5"/><path d="M0.8 6h10.4M6 0.6c-2.4 2.8-2.4 8 0 10.8M6 0.6c2.4 2.8 2.4 8 0 10.8" fill="none" stroke="#fff" stroke-width="0.7"/></svg>
          www.maplehollowmassage.example
        </li>
      </ul>
    </div>
  </section>

  <section class="card card--back" aria-label="Business card back">
    <p class="back-title">Maple Hollow<span>Canine Massage</span></p>
  </section>
</body>
</html>
```